Business Card Design Project

I am looking for a classy business card design for a product design consultancy. We specialize in Product Design, Prototyping, and Manufacturing Consulting. Products that we design range from consumer electronics to household products all the way to sporting goods. We are based in Arizona and called "Pelican Forge Studio." We like to have fun and goof off as much as we like to create new products. We are young and energetic so we would like our business cards to reflect that. We already have a logo that we would like to implement into the card design. A plain rectangular business card is boring so feel free to get creative, but please, no avocado shaped cards (it's far too literal). Also feel free to play around with textured card stocks or plastic. The final design that we choose will pay attention to all of the little details. Our cards will need to be 2 sided. We're giving you guys free reign to design as you would like. Please have fun with this, it will reflect in our business card.

Thanks guys,
Pelican Forge Studio Team
Updates

Industry/Entity Type

Electronics

Requirements
Must have
• We would like to have a spot UV coating somewhere on the business card design if possible.
Nice to have
• Let's see some designs with custom shapes rather than typical rectangular business cards but please no avocado shaped cards, thanks. Also play around with textured card socks.

Files

```html
<!DOCTYPE html>
<html lang="en">
<head>
<meta charset="utf-8">
<title>Pelican Forge Studio – Business Card</title>
<link rel="stylesheet" href="https://fonts.googleapis.com/css2?family=Montserrat:wght@400;500;700&display=swap">
<style>
  :root {
    --stage: #eceae6;
    --card-white: #ffffff;
    --card-shade: #f1f1f1;
    --leaf: #7cc242;
    --leaf-light: #d9f56a;
    --leaf-deep: #5fa82b;
    --ink: #2b2b2b;
    --ink-soft: #4a4a4a;
    --rule: #d6d6d6;
    --social: #3d86b8;
  }
  * { box-sizing: border-box; margin: 0; padding: 0; }
  html, body {
    width: 1200px; height: 840px; overflow: hidden;
    background: var(--stage);
    font-family: "Montserrat", sans-serif;
  }
  .canvas {
    position: relative; width: 1200px; height: 840px;
  }
  .card {
    position: absolute; top: 270px;
    width: 520px; height: 300px;
    border-radius: 22px;
    box-shadow: 0 10px 28px rgba(0,0,0,.14);
    overflow: hidden;
  }
  /* front side */
  .card--front {
    left: 60px;
    background: linear-gradient(160deg, var(--card-white) 55%, var(--card-shade));
  }
  .brand {
    position: absolute; top: 40px; left: 150px;
    display: flex; align-items: center; gap: 10px;
    color: var(--leaf); font-size: 24px; font-weight: 500;
  }
  .brand__dot {
    width: 18px; height: 18px; border-radius: 50%; background: currentColor;
  }
  .person { position: absolute; top: 104px; left: 60px; }
  .person__name {
    font-size: 17px; font-weight: 700; letter-spacing: .04em; color: var(--ink);
  }
  .person__title {
    font-size: 11px; color: var(--leaf); margin-top: 3px;
  }
  .contact {
    position: absolute; top: 152px; left: 60px;
    padding-left: 10px; border-left: 1px solid var(--rule);
    font-size: 12.5px; line-height: 1.6; color: var(--ink-soft);
    list-style: none;
  }
  .contact__label { color: var(--leaf); font-weight: 500; margin-right: 4px; }
  .social {
    position: absolute; right: 40px; bottom: 32px;
    display: flex; gap: 10px;
  }
  .social__dot {
    width: 14px; height: 14px; border-radius: 50%; background: var(--social);
  }
  /* back side */
  .card--back {
    left: 620px;
    background: var(--leaf);
  }
  .card__glow {
    position: absolute; inset: 0;
    background: radial-gradient(circle at 22% 18%, var(--leaf-light) 0, rgba(217,245,106,.55) 22%, rgba(124,194,66,0) 48%);
  }
  .brand--back {
    top: auto; left: auto; right: 40px; bottom: 44px;
    color: var(--card-white);
  }
</style>
</head>
<body>
<main class="canvas">

  <section class="card card--front" aria-label="Business card front">
    <div class="brand"><span class="brand__dot"></span>Pelican Forge Studio</div>

    <div class="person">
      <p class="person__name">DANA WHITLOCK</p>
      <p class="person__title">President</p>
    </div>

    <ul class="contact">
      <li><span class="contact__label">P.</span>480.555.0142</li>
      <li><span class="contact__label">M.</span>602.555.0187</li>
      <li>dana@pelicanforgestudio.com</li>
      <li>www.pelicanforgestudio.com</li>
    </ul>

    <div class="social" aria-label="Social profiles">
      <span class="social__dot"></span>
      <span class="social__dot"></span>
      <span class="social__dot"></span>
    </div>
  </section>

  <section class="card card--back" aria-label="Business card back">
    <div class="card__glow" role="img" aria-label="Spot UV gloss accent in light green"></div>
    <div class="brand brand--back"><span class="brand__dot"></span>Pelican Forge Studio</div>
  </section>

</main>
</body>
</html>
```